Kestrel.vc needs a better website design!

We need a new and better website for Kestrel.vc. We're a Canadian venture capital firm that invests in innovative entrepreneurs. We compete against the following websites: lumora.vc, brightvalefund.ca, osprovc.com, and tessara.vc. We're a diverse group of partners and we're dedicated to the founders we invest in.
Updates

I don’t really like stock photos of random people as part of the website design…so please try to stay away from using those images. Thanks, Owen

Target Market(s)

Canadian entrepreneurs and investors

Industry/Entity Type

Venture capital, finance, investment, entrepreneurship

Coding

Coded - Design and coding required

Number of Pages Required

4 page

Font styles to use
Sans Serif

Colors

Designer to choose colors to be used in the design.

Requirements
Must have
• Clean crisp overall design. Fast and to the point.
Nice to have
• Check out www.kestrel.vc - I did it myself and it is too basic and too wordy.
Should not have
• No stock images with random people in them! Not too wordy or with too many large images that are slow to load.

```html
<!DOCTYPE html>
<html lang="en">
<head>
<meta charset="utf-8">
<title>Kestrel.vc</title>
<link rel="stylesheet" href="https://fonts.googleapis.com/css2?family=Poppins:wght@300;400;500;600;700&display=swap">
<style>
:root{
  --green:#6e9a2c;
  --ink:#2b2b2b;
  --muted:#666;
  --line:#e4e4e4;
  --footer:#f4f4f4;
  --white:#fff;
  --hero-top:#5d6b73;
  --hero-mid:#3e5a4e;
  --hero-bot:#2e5a5c;
}
*{box-sizing:border-box;margin:0;padding:0}
html,body{width:1200px;height:2296px;overflow:hidden}
body{font-family:"Poppins",sans-serif;color:var(--ink);background:var(--white);position:relative}
.site-header{height:112px;display:flex;align-items:center;justify-content:space-between;padding:0 180px 0 172px}
.brand{display:flex;align-items:center;gap:10px;font-weight:700;font-size:26px;color:var(--green)}
.brand-dot{width:16px;height:16px;border-radius:50%;background:var(--green)}
.main-nav{display:flex;gap:54px;font-size:15px;color:var(--ink)}
.main-nav a{color:inherit;text-decoration:none;padding-bottom:6px}
.main-nav a.active{color:var(--green);border-bottom:2px solid var(--green)}
.hero{position:relative;height:568px;background:linear-gradient(180deg,var(--hero-top) 0%,var(--hero-mid) 55%,var(--hero-bot) 100%);color:var(--white);text-align:center}
.hero-text{position:absolute;top:120px;left:160px;right:160px;font-size:28px;line-height:1.55;font-weight:500}
.stats-title{position:absolute;top:332px;left:0;right:0;font-size:19px}
.stats-title::after{content:"";display:block;width:180px;height:1px;background:rgba(255,255,255,.7);margin:12px auto 0}
.stats{position:absolute;top:375px;left:0;right:0;display:flex;justify-content:center;gap:70px}
.stat{display:flex;align-items:center;gap:10px;text-align:left}
.stat-num{font-size:46px;font-weight:600}
.stat-label{font-size:13px;line-height:1.25}
.intro{padding-top:60px;text-align:center}
.section-title{font-size:30px;font-weight:500;line-height:1.45}
.services{display:flex;justify-content:center;gap:32px;margin-top:44px}
.service-card{width:436px;height:280px;border:1px solid var(--line);box-shadow:0 4px 16px rgba(0,0,0,.07);padding:44px 40px;text-align:left}
.service-card svg{display:block;margin-bottom:18px}
.service-card p{font-size:18px;line-height:1.55;color:var(--muted)}
.portfolio{margin-top:98px;text-align:center}
.portfolio .section-title{font-size:28px}
.logo-grid{width:900px;margin:34px auto 0;display:grid;grid-template-columns:repeat(5,1fr);gap:28px 26px}
.logo-tile{height:66px;border:1px solid var(--line);box-shadow:0 2px 8px rgba(0,0,0,.05);display:flex;align-items:center;justify-content:center;font-size:18px;font-weight:600;color:#333;white-space:nowrap}
.contact-band{position:absolute;top:1530px;left:0;width:1200px;height:450px;background:linear-gradient(180deg,#3f4a45 0%,#2f3f36 60%,#26332c 100%);color:var(--white);text-align:center;display:flex;flex-direction:column;justify-content:center;font-size:40px;font-weight:300;line-height:1.35}
.site-footer{position:absolute;top:1980px;left:0;width:1200px;height:268px;background:var(--footer);display:flex;padding:50px 0 0 200px}
.footer-brand{width:340px;display:flex;flex-direction:column;align-items:flex-start;gap:12px;font-size:30px;font-weight:700;color:var(--green)}
.footer-brand .brand-dot{width:44px;height:44px}
.footer-col h4{font-size:18px;font-weight:600;margin-bottom:12px}
.links{width:320px}
.links ul{list-style:none;font-size:14px;color:var(--muted);line-height:2}
.links li::before{content:"›";margin-right:10px;color:var(--green)}
.contact-row{font-size:14px;display:flex;gap:40px;margin-bottom:26px}
.socials{display:flex;gap:10px;margin-top:8px}
.socials span{width:26px;height:26px;border-radius:50%;background:#2a7ab8}
.copyright{position:absolute;top:2248px;left:0;width:1200px;height:48px;background:var(--green);color:var(--white);font-size:13px;display:flex;align-items:center;justify-content:center}
</style>
</head>
<body>
<header class="site-header">
  <div class="brand"><span class="brand-dot"></span>KESTREL.VC</div>
  <nav class="main-nav"><a class="active">Home</a><a>What</a><a>Who</a><a>Portfolio</a></nav>
</header>

<section class="hero" role="img" aria-label="Mountain lake landscape with forested slopes and misty peaks">
  <p class="hero-text">Kestrel.vc is a venture capital firm that invests in innovative seed-stage technology companies in Western Canada focused on B2B and SaaS markets.</p>
  <p class="stats-title">Kestrel.vc in numbers</p>
  <div class="stats">
    <div class="stat"><span class="stat-num">10</span><span class="stat-label">Portfolio<br>companies</span></div>
    <div class="stat"><span class="stat-num">7</span><span class="stat-label">Follow-on<br>financings</span></div>
    <div class="stat"><span class="stat-num">100<sup style="font-size:18px">+</sup></span><span class="stat-label">Employees</span></div>
  </div>
</section>

<section class="intro">
  <h2 class="section-title">We are serial entrepreneurs and venture<br>capital investors who provide</h2>
  <div class="services">
    <article class="service-card">
      <svg width="80" height="64" viewBox="0 0 80 64" fill="none" stroke="#555" stroke-width="2"><rect x="6" y="40" width="10" height="20"/><rect x="22" y="30" width="10" height="30"/><rect x="38" y="22" width="10" height="38"/><rect x="54" y="14" width="10" height="46"/><path d="M4 30 L30 12 L46 18 L72 4" stroke="var(--green)"/><path d="M64 4 L72 4 L72 12" stroke="var(--green)"/></svg>
      <p>Mentoring and strategic advice to help you grow your company quickly and efficiently</p>
    </article>
    <article class="service-card">
      <svg width="70" height="64" viewBox="0 0 70 64" fill="none" stroke="#555" stroke-width="2"><circle cx="24" cy="22" r="14"/><circle cx="44" cy="40" r="16" stroke="var(--green)"/><path d="M44 30 v20 M38 35 h9 a3 3 0 0 1 0 6 h-6 a3 3 0 0 0 0 6 h9" stroke="var(--green)"/></svg>
      <p>Investor introductions to help you raise additional follow-on funding for your startup</p>
    </article>
  </div>
</section>

<section class="portfolio">
  <h2 class="section-title">Check out our innovative portfolio companies!</h2>
  <div class="logo-grid">
    <div class="logo-tile">Halcyra</div>
    <div class="logo-tile">Tovik</div>
    <div class="logo-tile">Meridel</div>
    <div class="logo-tile">Quorra</div>
    <div class="logo-tile">Basalt</div>
    <div class="logo-tile">Fernly</div>
    <div class="logo-tile">Onyxa</div>
    <div class="logo-tile">Corvane</div>
    <div class="logo-tile">Pellum</div>
    <div class="logo-tile">Ardent Bay</div>
  </div>
</section>

<section class="contact-band" role="img" aria-label="Dark misty mountain range backdrop">
  <p>Contact us today<br>If you have what we're looking for</p>
</section>

<footer class="site-footer">
  <div class="footer-brand"><span class="brand-dot"></span>KESTREL.VC</div>
  <div class="footer-col links">
    <h4>Quick Links</h4>
    <ul><li>Home</li><li>What</li><li>Who</li><li>Portfolio</li></ul>
  </div>
  <div class="footer-col">
    <h4>Get In Touch</h4>
    <div class="contact-row"><strong>Email</strong><span>info@kestrel.vc</span></div>
    <h4>Follow Us</h4>
    <div class="socials"><span></span><span></span></div>
  </div>
</footer>
<div class="copyright">Copyright © 2020 Kestrel.vc - All Rights Reserved</div>
</body>
</html>
```